Website Design for Law Firm

We need a fresh new website design for our client 'Torvek Legal' who specialises as a Criminal, Traffic & Civil Lawyer in Perth, Western Australia. We are looking for a very clean, professional and elegant look for the website, a presence of power and class needed as he deals with high end clients. Black, Silver and hints of gold need to run through the design without making the site look too dark. We are after a very modern, spacious web look, use of large readable text with links to social media (such as Facebook, Google+, Twitter, LinkedIn) to stand out and his contact details to be made very predominate.

Reason: Public holidays here in Australia, need more business hours to discuss designs with client.

Reason: Client needs more time to look through designs.

Reason: Client is going over last of designs. Design will be picked early next week!

Law Firm

```html
<!DOCTYPE html>
<html lang="en">
<head>
<meta charset="utf-8">
<title>Torvek Legal</title>
<link href="https://fonts.googleapis.com/css2?family=Open+Sans:ital,wght@0,400;0,600;0,700;0,800&family=Courgette&display=swap" rel="stylesheet">
<style>
:root{
  --gold:#e8b70c;
  --gold-deep:#d9a800;
  --ink:#231f20;
  --text:#222222;
  --muted:#8a8a8a;
  --panel:#dddddd;
  --rule:#b9b9b9;
  --white:#ffffff;
  --icon-grey:#6e6e6e;
}
*{margin:0;padding:0;box-sizing:border-box}
html,body{width:1200px;height:900px;overflow:hidden;background:var(--white);font-family:"Open Sans",Arial,sans-serif;color:var(--text)}
.canvas{position:relative;width:1200px;height:900px}
.abs{position:absolute}

/* header */
.brand{left:332px;top:14px;display:flex;align-items:center;gap:8px}
.brand-mark{width:14px;height:14px;background:var(--ink)}
.brand-name{font-weight:800;font-size:27px;letter-spacing:-.5px;color:var(--ink);line-height:1}
.top-phone{left:755px;top:10px;display:flex;align-items:center;gap:4px;color:var(--gold);font-weight:700;font-size:17px}
.nav{left:603px;top:36px;display:flex;font-size:8.5px;text-transform:uppercase}
.nav a{display:block;height:23px;line-height:23px;padding:0 9px;color:var(--text);text-decoration:none}
.nav a.active{background:var(--gold);color:var(--ink)}
.tagline{left:256px;width:689px;top:74px;text-align:center;font-family:"Courgette",cursive;font-size:14px;line-height:18px;color:var(--muted)}

/* hero */
.hero{left:256px;top:126px;width:689px;height:254px;background:linear-gradient(90deg,#ece2dc 0%,#eadbd3 45%,#e6d2c6 100%)}
.hero-photo{position:absolute;left:310px;top:0;width:379px;height:254px;background:radial-gradient(ellipse at 55% 60%,#b8763a 0%,#d9a888 35%,#efd7c8 75%,#f0ddd0 100%)}
.hero-kicker{position:absolute;left:171px;top:93px;font-weight:700;font-size:14px;color:var(--ink)}
.hero-title{position:absolute;left:77px;top:96px;font-weight:700;font-size:54px;letter-spacing:-1px;color:var(--ink);line-height:64px}
.hero-copy{position:absolute;left:82px;top:153px;width:170px;font-size:6.5px;line-height:9.5px;color:var(--ink)}

/* features */
.features{left:256px;top:380px;width:689px;height:95px;background:var(--ink)}
.feature{position:absolute;top:18px;width:165px}
.feature-head{display:flex;align-items:center;gap:10px;color:var(--gold);font-weight:700;font-size:10px;height:20px}
.feature p{margin-top:6px;font-size:6.3px;line-height:9.5px;color:var(--gold)}

/* panels */
.panel{left:256px;width:689px;background:var(--panel)}
.panel-welcome{top:475px;height:142px;border-bottom:1px solid var(--rule)}
.panel-testimonials{top:618px;height:142px}
.section-title{position:absolute;font-weight:700;font-size:10px;color:var(--ink)}
.portrait{position:absolute;left:77px;top:32px;width:123px;height:82px;border:2px solid var(--white);background:linear-gradient(135deg,#6b3a22 0%,#3a2a22 50%,#1e1e26 100%)}
.welcome-copy{position:absolute;left:206px;top:30px;width:203px;font-size:6.3px;line-height:9.8px;color:var(--ink)}
.law-list{position:absolute;left:449px;top:28px;list-style:none;font-size:6.3px;color:var(--ink)}
.law-list li{height:13.5px;display:flex;align-items:center;gap:8px}
.law-list li::before{content:"";width:5px;height:5px;background:var(--ink);transform:rotate(45deg)}
.quote{position:absolute;left:104px;top:35px;width:210px;font-family:"Courgette",cursive;font-size:6px;line-height:9.6px;color:var(--ink)}
.quote-mark{position:absolute;color:#a9a9a9;font-family:Georgia,serif;font-size:46px;line-height:1}
.quote-author{position:absolute;left:262px;top:99px;font-weight:700;font-size:7px;color:var(--gold)}
.signup{position:absolute;left:449px;top:42px;display:flex;gap:11px}
.signup-input{width:112px;height:16px;background:var(--white);border:1px solid #cfcfcf;font-size:6px;padding-left:4px;line-height:14px;color:#555}
.signup-button{width:51px;height:16px;background:#0d0d0d;color:var(--gold);font-size:7px;line-height:16px;text-align:center}

/* footer */
.footer{left:256px;top:760px;width:689px;height:140px;background:var(--ink)}
.footer-col{position:absolute;top:15px}
.footer-col h3{font-size:10px;font-weight:700;color:var(--gold);margin-bottom:9px}
.footer-col li{list-style:none;font-size:6.3px;color:var(--white);height:13.5px;line-height:13.5px}
.footer-phone{position:absolute;right:67px;top:11px;text-align:right;color:var(--gold);font-weight:700;font-size:26px;line-height:32px}
.footer-hours{position:absolute;right:67px;top:40px;color:var(--icon-grey);font-weight:700;font-size:13px}
.fan-label{position:absolute;left:449px;top:73px;color:var(--gold);font-weight:700;font-size:10px}
.social{position:absolute;top:70px;width:22px;height:22px;background:var(--icon-grey)}
.footer-rule{position:absolute;left:77px;right:66px;top:107px;border-top:1px solid #4a4546}
.copyright{position:absolute;left:0;width:689px;top:116px;text-align:center;font-size:5.8px;color:var(--gold)}
</style>
</head>
<body>
<div class="canvas">

  <header>
    <div class="abs brand"><span class="brand-mark"></span><span class="brand-name">TORVEK LEGAL</span></div>
    <div class="abs top-phone">
      <svg width="14" height="16" viewBox="0 0 14 16" aria-hidden="true"><path d="M3 1 L6 4 L4.5 6 Q6 10 9 11.5 L11 10 L14 13 L11.5 15.5 Q5 14 1.5 6 Q1 3 3 1Z" fill="var(--gold)"/></svg>
      <span>1-800-5550147</span>
    </div>
    <nav class="abs nav">
      <a class="active" href="#">Home</a><a href="#">About</a><a href="#">Services</a><a href="#">People</a><a href="#">Careers</a><a href="#">Contact Us</a>
    </nav>
    <p class="abs tagline">Torvek Legal believe that client's success determines our own. So we ensure both by<br>collaborating with our clients to achieve thair goals.</p>
  </header>

  <section class="abs hero">
    <div class="hero-photo" role="img" aria-label="Wooden judge's gavel resting on a sound block, warm blurred courtroom background"></div>
    <div class="hero-kicker">Torvek Legal</div>
    <div class="hero-title">Lawers</div>
    <p class="hero-copy">Lorem Ipsum is simply dummy text of the printing and typesetting industry. Lorem Ipsum has been the industry's standard dummy Lorem Ipsum.</p>
  </section>

  <section class="abs features">
    <div class="feature" style="left:77px">
      <div class="feature-head">
        <svg width="20" height="18" viewBox="0 0 20 18" aria-hidden="true"><g stroke="var(--gold)" stroke-width="1.4" fill="none"><path d="M10 1V16M5 17H15M2 4H18"/><path d="M2 4L0 10H4Z M18 4L16 10H20Z"/></g></svg>
        <span>Book an Appointment</span>
      </div>
      <p>Lorem Ipsum is simply dummy text of the printing and typesetting industry. Lorem Ipsum has been the industry's standard dummy Lorem Ipsum.</p>
    </div>
    <div class="feature" style="left:261px">
      <div class="feature-head">
        <svg width="14" height="20" viewBox="0 0 14 20" aria-hidden="true"><circle cx="7" cy="7" r="6" fill="var(--gold)"/><rect x="4" y="12" width="6" height="6" rx="1" fill="var(--gold)"/></svg>
        <span>Quality Legal Solutions</span>
      </div>
      <p>Lorem Ipsum is simply dummy text of the printing and typesetting industry. Lorem Ipsum has been the industry's standard dummy Lorem Ipsum.</p>
    </div>
    <div class="feature" style="left:449px">
      <div class="feature-head">
        <svg width="16" height="18" viewBox="0 0 16 18" aria-hidden="true"><path d="M3 1H13V6Q13 11 8 11Q3 11 3 6Z" fill="var(--gold)"/><path d="M3 3H0.8Q1 7 4 8M13 3H15.2Q15 7 12 8" stroke="var(--gold)" stroke-width="1.2" fill="none"/><rect x="7" y="11" width="2" height="3" fill="var(--gold)"/><rect x="4" y="14" width="8" height="3" fill="var(--gold)"/></svg>
        <span>Award Winnings</span>
      </div>
      <p>Lorem Ipsum is simply dummy text of the printing and typesetting industry. Lorem Ipsum has been the industry's standard dummy Lorem Ipsum.</p>
    </div>
  </section>

  <section class="abs panel panel-welcome">
    <h2 class="section-title" style="left:77px;top:10px">Welcome Dear Visiter!</h2>
    <div class="portrait" role="img" aria-label="Portrait of a lawyer in a suit in front of a bookshelf"></div>
    <p class="welcome-copy">Nunc rhoncus, tellus ultrices fermentum fringilla, justo lectus hendrerit erat, sit amet hendrerit velit est quis lacus. Nunc auctor nisi justo, et gravida nisl posuere sed. Mauris quis dui nec purus adipiscing elementum et ac ligula. Proin ut faucibus tellus. In euismod, velit nec imperdiet semper, felis augue rutrum dolor, non sodales urna orci ut metus. Morbi magna ligula, congue vel ipsum at, accumsan porttitor nisl. In volutpat nulla nibh, at dignissim sapien dictum a. Ut venenatis vestibulum purus ac euismod. Ut ultricies, nunc tempor elementum gravida, eros mi viverra diam, ut placerat risus magna eu</p>
    <h2 class="section-title" style="left:449px;top:10px">Areas of Law</h2>
    <ul class="law-list">
      <li>Elder Abuse Cases</li><li>Employment Law</li><li>Family Law</li><li>Immigration Law</li><li>Insurance Law</li><li>Malpractice Law</li><li>Real Property Law</li><li>Securities Law</li>
    </ul>
  </section>

  <section class="abs panel panel-testimonials">
    <h2 class="section-title" style="left:77px;top:8px">Client Testimonials</h2>
    <span class="quote-mark" style="left:77px;top:28px">&ldquo;</span>
    <p class="quote">Nunc rhoncus, tellus ultrices fermentum fringilla, justo lectus hendrerit erat, sit amet hendrerit velit est quis lacus. Nunc auctor nisi justo, et gravida nisl posuere sed. Mauris quis dui nec purus adipiscing elementum et ac ligula. Proin ut faucibus tellus. In euismod, velit nec imperdiet semper, felis augue rutrum dolor, non sodales urna orci ut metus. Morbi magna ligula, congue vel ipsum at, accumsan porttitor</p>
    <span class="quote-mark" style="left:306px;top:77px">&rdquo;</span>
    <div class="quote-author">Mark Ellison</div>
    <h2 class="section-title" style="left:448px;top:15px">Newsletter Sign-up:</h2>
    <div class="signup"><div class="signup-input">Enter Your Email...</div><div class="signup-button">Subcribe</div></div>
  </section>

  <footer class="abs footer">
    <div class="footer-col" style="left:77px"><h3>About US</h3><ul><li>Company Info</li><li>Services</li><li>Partmet</li><li>fermentum</li></ul></div>
    <div class="footer-col" style="left:180px"><h3>Advice</h3><ul><li>Company Info</li><li>Services</li><li>Partmet</li><li>fermentum</li></ul></div>
    <div class="footer-col" style="left:278px"><h3>Join in</h3><ul><li>Company Info</li><li>Services</li><li>Partmet</li><li>fermentum</li></ul></div>
    <div class="footer-col" style="left:374px"><h3>Support</h3><ul><li>Company Info</li><li>Services</li><li>Partmet</li><li>fermentum</li></ul></div>
    <div class="footer-phone">1-800-5550147</div>
    <div class="footer-hours">24/7</div>
    <div class="fan-label">Fan Pages:</div>
    <span class="social" style="left:546px" aria-label="Social page link"></span>
    <span class="social" style="left:573px" aria-label="Social page link"></span>
    <span class="social" style="left:600px" aria-label="Social page link"></span>
    <div class="footer-rule"></div>
    <p class="copyright">&copy; 2014 Torvek Legal. All rights reserved.</p>
  </footer>

</div>
</body>
</html>
```